Goal Planning Work Sheet

Design a better Goal Planning Worksheet that is fillable

Target Market(s)

People looking to make an important change

Industry/Entity Type

Work

Requirements
Must have
• Fillable pdf form
• Exceptional Design

```html
<!DOCTYPE html>
<html lang="en">
<head>
<meta charset="utf-8">
<title>I'm Being Smarter Now – Goal Planning Worksheet</title>
<link rel="stylesheet" href="https://fonts.googleapis.com/css2?family=Open+Sans:wght@300;400;600;700&display=swap">
<style>
  :root {
    --navy: #1a4c82;
    --red: #d7192a;
    --sidebar: #e9e9eb;
    --paper: #ffffff;
    --backdrop: #dcdcdc;
    --ink: #1a4c82;
    --box-line: #2b5d95;
  }
  * { box-sizing: border-box; margin: 0; padding: 0; }
  html, body { width: 1200px; height: 898px; overflow: hidden; }
  body {
    background: var(--backdrop);
    font-family: "Open Sans", Arial, sans-serif;
    color: var(--ink);
  }
  .worksheet {
    position: absolute;
    left: 290px; top: 19px;
    width: 620px; height: 860px;
    background: var(--paper);
    overflow: hidden;
    box-shadow: 0 6px 18px rgba(0,0,0,.18);
  }
  .worksheet__header { position: absolute; left: 0; top: 0; width: 620px; height: 190px; z-index: 1; }
  .worksheet__title {
    position: absolute; right: 28px; top: 30px; z-index: 2;
    border: 1px solid #fff; color: #fff;
    font-weight: 300; font-size: 19px; letter-spacing: .3px;
    padding: 8px 16px;
  }
  .emblem {
    position: absolute; left: 92px; top: 88px; z-index: 2;
    width: 104px; height: 104px; border-radius: 50%;
    background: radial-gradient(circle at 45% 40%, #e9f7f8 0%, #a8dce2 55%, #5fb7c3 100%);
    border: 3px solid #d9eef0;
    box-shadow: 0 2px 5px rgba(0,0,0,.25);
  }
  .sidebar {
    position: absolute; left: 0; top: 180px;
    width: 205px; height: 660px;
    background: var(--sidebar);
    padding: 44px 14px 0 14px;
  }
  .sidebar__section { margin-bottom: 20px; }
  .sidebar__tab {
    display: inline-block; background: var(--navy); color: #fff;
    font-size: 10.5px; font-weight: 600;
    padding: 3px 34px 3px 8px;
    clip-path: polygon(0 0, 100% 0, 88% 100%, 0 100%);
    margin-bottom: 5px; min-width: 150px;
  }
  .sidebar__list { list-style: none; font-size: 10px; line-height: 1.22; }
  .sidebar__list li { position: relative; padding-left: 10px; }
  .sidebar__list li::before {
    content: ""; position: absolute; left: 0; top: 3px;
    border-left: 6px solid var(--navy);
    border-top: 3.5px solid transparent; border-bottom: 3.5px solid transparent;
  }
  .sidebar__list b { font-weight: 700; }
  .planner {
    position: absolute; left: 218px; top: 150px; width: 382px; z-index: 2;
  }
  .field { margin-bottom: 10px; }
  .field__label {
    background: var(--navy); color: #fff;
    font-size: 10px; line-height: 1.25; padding: 5px 8px;
  }
  .field__area {
    border: 1px solid var(--box-line); border-top: none;
    background: #fff; margin: 0 4px;
  }
  .field--imagine .field__area { height: 100px; }
  .field--smart .field__area { height: 126px; }
  .field--roadblocks .field__area { height: 106px; }
  .field--team .field__area { height: 64px; }
  .field--evaluate .field__area { height: 60px; }
  .worksheet__footer { position: absolute; left: 0; bottom: 0; width: 620px; height: 70px; z-index: 1; }
</style>
</head>
<body>
  <main class="worksheet">
    <aside class="sidebar">
      <section class="sidebar__section">
        <div class="sidebar__tab">Strength Spotting</div>
        <ul class="sidebar__list">
          <li><b>Wisdom:</b> Cognitive Creativity Curiosity Judgment Love of Learning Perspective</li>
          <li><b>Courage:</b> Bravery Perseverance Honesty Zest</li>
          <li><b>Humanity:</b> Love Kindness Social Intelligence Teamwork</li>
          <li><b>Justice:</b> Fairness Leadership</li>
          <li><b>Temperance:</b> Forgiveness Humility Prudence Self-Regulation</li>
          <li><b>Transcendence:</b> Appreciation Beauty &amp; Excellence Gratitude Hope Humor Spirituality</li>
        </ul>
      </section>
      <section class="sidebar__section">
        <div class="sidebar__tab">Fear</div>
        <ul class="sidebar__list">
          <li>Fuse To Thoughts and Feelings</li>
          <li>Excessive Thinking</li>
          <li>Attractors Negative Emotional</li>
          <li>Run Away &amp; Avoidance</li>
        </ul>
      </section>
      <section class="sidebar__section">
        <div class="sidebar__tab">Dare</div>
        <ul class="sidebar__list">
          <li><b>Defuse:</b> Notice, Name, Normalize</li>
          <li><b>Acceptance:</b> Allow, Appreciate</li>
          <li>Reinforce Skills &amp; Support</li>
          <li>Enjoy Values</li>
        </ul>
      </section>
      <section class="sidebar__section">
        <div class="sidebar__tab">Problem Solving Process</div>
        <ul class="sidebar__list">
          <li>Domain of Problem</li>
          <li>Team Gathered</li>
          <li>Values Focus</li>
          <li>Imagine, Move, Be</li>
          <li>Define Problem, Cause, Solutions</li>
          <li>Plan-SMARTER Goals</li>
          <li>Resources &amp; Resourcefulness</li>
          <li>Practice, Rehearse</li>
          <li>Act Communicate</li>
          <li>Evaluate Revise</li>
        </ul>
      </section>
    </aside>

    <svg class="worksheet__header" viewBox="0 0 620 190" aria-hidden="true">
      <path d="M0 0 H620 V70 C520 120 420 100 300 118 C200 132 120 130 0 180 Z" fill="var(--navy)"/>
      <path d="M0 180 C120 130 200 132 300 118 C420 100 520 120 620 70 V80 C520 130 420 110 300 128 C200 142 120 140 0 192 Z" fill="var(--red)"/>
    </svg>
    <div class="worksheet__title">I'M BEING SMARTER NOW</div>
    <div class="emblem" role="img" aria-label="Compass emblem with a heart at its centre"></div>

    <section class="planner">
      <div class="field field--imagine">
        <div class="field__label">Imagine and Move (motion creates emotion) Being the person I want to be, Values, Character Strengths:</div>
        <div class="field__area"></div>
      </div>
      <div class="field field--smart">
        <div class="field__label">Specific Small Meaningful Measurable Actionable Attainable Timeline Now:</div>
        <div class="field__area"></div>
      </div>
      <div class="field field--roadblocks">
        <div class="field__label">Roadblocks Resources Rewards Ramification:</div>
        <div class="field__area"></div>
      </div>
      <div class="field field--team">
        <div class="field__label">Team Roles:</div>
        <div class="field__area"></div>
      </div>
      <div class="field field--evaluate">
        <div class="field__label">Evaluate, Emotions, Revise, Resilient</div>
        <div class="field__area"></div>
      </div>
    </section>

    <svg class="worksheet__footer" viewBox="0 0 620 70" aria-hidden="true">
      <path d="M0 40 C200 36 420 30 620 6 V14 C420 38 200 44 0 48 Z" fill="var(--red)"/>
      <path d="M0 48 C200 44 420 38 620 14 V70 H0 Z" fill="var(--navy)"/>
    </svg>
  </main>
</body>
</html>
```